Cover for Where the Quiet River Bends Beyond Our Morning

Cover for a book that describes everything that happens to a person, from pre-birth life plans through growing in compassion and wisdom to death and living in the afterlife. The information is revealed in messages from people living in the life after this life. The title is Lanterns Along the Hidden Stair of Every Soul: Gathered from Voices Dwelling in the Further Meadow. Author is T. Morven Ashdale. Book size is 6 by 9.

Target Market(s)

General

Font styles to use
Serif

```html
<!DOCTYPE html>
<html lang="en">
<head>
<meta charset="utf-8">
<title>Lanterns Along the Hidden Stair of Every Soul — Cover</title>
<link rel="stylesheet" href="https://fonts.googleapis.com/css2?family=Cinzel+Decorative:wght@700;900&family=Cinzel:wght@600&family=Lato:wght@400&display=swap">
<style>
  :root {
    --page-bg: #f4f2ee;
    --sky-blue: #7fa6d8;
    --sky-pink: #e9c6ea;
    --sun-white: #fffdf6;
    --glow-orange: #f6b45a;
    --wood-light: #c9a877;
    --wood-mid: #8c7556;
    --wood-dark: #5a4a38;
    --grass: #6f7f3e;
    --carved-ink: rgba(38, 28, 18, 0.82);
    --author-ink: #1c1712;
  }
  * { margin: 0; padding: 0; box-sizing: border-box; }
  html, body {
    width: 1200px; height: 647px; overflow: hidden;
    background: var(--page-bg);
  }
  .canvas {
    position: relative; width: 1200px; height: 647px;
    display: flex; justify-content: center; align-items: center;
  }
  .book-cover {
    position: relative; width: 431px; height: 647px; overflow: hidden;
    box-shadow: 0 4px 18px rgba(0,0,0,0.18);
  }
  .cover-photo {
    position: absolute; inset: 0;
    background:
      radial-gradient(ellipse 55% 30% at 50% 6%, var(--sun-white) 0%, rgba(255,253,246,0.9) 40%, rgba(255,253,246,0) 100%),
      linear-gradient(90deg, rgba(111,127,62,0.55) 0%, rgba(111,127,62,0) 18%, rgba(111,127,62,0) 82%, rgba(111,127,62,0.55) 100%),
      linear-gradient(180deg,
        var(--sky-blue) 0%,
        var(--sky-pink) 8%,
        var(--sun-white) 16%,
        #fbe3b4 24%,
        var(--glow-orange) 32%,
        var(--wood-light) 42%,
        var(--wood-mid) 62%,
        #9a8565 78%,
        var(--wood-dark) 100%);
  }
  .title-block {
    position: absolute; left: 0; right: 0; top: 250px;
    text-align: center; color: var(--carved-ink);
    font-family: "Cinzel Decorative", serif; font-weight: 900;
    line-height: 1;
  }
  .title-line { display: block; }
  .title-line--1 { font-size: 28px; margin-bottom: 6px; }
  .title-line--2 { font-size: 30px; margin-bottom: 8px; }
  .title-line--3 { font-size: 34px; margin-bottom: 10px; }
  .title-line--4 { font-size: 48px; letter-spacing: 2px; }
  .subtitle {
    position: absolute; left: 24px; right: 24px; top: 440px;
    text-align: center; color: var(--carved-ink);
    font-family: "Cinzel", serif; font-weight: 600;
    line-height: 1.25;
  }
  .subtitle-line { display: block; }
  .subtitle-line--1 { font-size: 15px; letter-spacing: 3px; font-style: italic; }
  .subtitle-line--2 { font-size: 18px; letter-spacing: 0.5px; }
  .author {
    position: absolute; right: 48px; top: 522px;
    font-family: "Lato", sans-serif; font-weight: 400;
    font-size: 20px; letter-spacing: 0.5px; color: var(--author-ink);
    text-transform: uppercase;
  }
</style>
</head>
<body>
  <main class="canvas">
    <article class="book-cover">
      <div class="cover-photo" role="img" aria-label="Photograph of weathered wooden steps with handrails climbing a grassy hill toward a bright sunlit sky"></div>
      <h1 class="title-block">
        <span class="title-line title-line--1">Lanterns Along</span>
        <span class="title-line title-line--2">the Hidden Stair</span>
        <span class="title-line title-line--3">of Every</span>
        <span class="title-line title-line--4">Soul</span>
      </h1>
      <p class="subtitle">
        <span class="subtitle-line subtitle-line--1">GATHERED FROM VOICES</span>
        <span class="subtitle-line subtitle-line--2">DWELLING IN THE FURTHER MEADOW</span>
      </p>
      <p class="author">T. Morven Ashdale</p>
    </article>
  </main>
</body>
</html>
```